ReDesign Website for a more Bold approach

Hello! I'd like to redesign my website: torvellacapital.com

I'd like to add one thing that's not on my website which is a blog. The design around the blog should be put time into as I will be putting out incredibly great content and want it to attract viewers.

I get a lot of inspiration from quondel.com (the way they flow the big statements across each screen, colors)
amberlit.vc (the simplicity behind the design is beautiful)

I like modern very simple but bold approaches.

I am going to attach my logo here and if it can be thought of when making the design of the website. Thanks!

Industry/Entity Type

Finance and Private Equity

Number of Pages Required

3 page

Font styles to use
Serif
Sans Serif

Colors
0054AA
0677BA
7BADD7
CADEEF
E8F1F8
0094D4
00A9DD
6FCCEA
C7EBF8
E9F6FB
00AB8E
00BBA5
67D7C9
C6EFE9
E9F9F6

Requirements
Must have
• My project must have a Home, Expertise, Story, Clients, Approach, Blog, Contact
Nice to have
• It would be nice to have these tabs reduced to 1-3 pages
Should not have
• My project must not have bright colors.

```html
<!DOCTYPE html>
<html lang="en">
<head>
<meta charset="utf-8">
<title>Torvella Capital</title>
<link href="https://fonts.googleapis.com/css2?family=Montserrat:wght@400;500;600;700;800&display=swap" rel="stylesheet">
<style>
:root{
  --navy:#0b1a3a;
  --ink:#10284c;
  --body:#3d4d66;
  --accent:#e8434b;
  --teal:#00bba5;
  --ghost:#e4e9f0;
  --frame:#7fc8d8;
  --line:#9cc9de;
  --white:#ffffff;
}
*{margin:0;padding:0;box-sizing:border-box}
html,body{width:1200px;height:4870px;overflow:hidden}
body{font-family:"Montserrat",sans-serif;color:var(--body);background:var(--white);position:relative}
.abs{position:absolute}
.btn{position:absolute;display:flex;align-items:center;justify-content:center;font-size:11px;font-weight:700;letter-spacing:1.2px;text-transform:uppercase;white-space:nowrap}
.btn-outline{border:2px solid var(--ink);color:var(--ink);background:var(--white)}
.section-title{position:absolute;left:0;width:1200px;text-align:center;font-weight:800;color:var(--ink);font-size:38px;letter-spacing:.5px;white-space:nowrap}
.ghost{position:absolute;left:0;width:1200px;text-align:center;font-weight:800;color:var(--ghost);font-size:44px;letter-spacing:1px;white-space:nowrap}

/* hero */
.hero{position:absolute;left:0;top:0;width:1200px;height:740px;background:linear-gradient(120deg,#08152f 0%,#0d2452 45%,#1a55b0 70%,#0b2a66 100%)}
.logo{position:absolute;font-weight:700;font-size:24px;color:var(--white);letter-spacing:.5px;white-space:nowrap}
.nav a{position:absolute;top:44px;font-size:11px;font-weight:600;color:var(--white);text-decoration:none;letter-spacing:.8px;white-space:nowrap}
.nav .active{border-bottom:2px solid var(--accent);padding-bottom:9px}
.nav .contact{top:34px;left:920px;width:138px;height:36px;border-radius:18px;background:var(--accent);display:flex;align-items:center;justify-content:center}
.hero-kicker{left:105px;top:268px;font-size:26px;letter-spacing:4px;color:var(--white);font-weight:400;white-space:nowrap}
.hero-title{left:105px;top:302px;font-size:46px;line-height:56px;font-weight:800;color:var(--white);letter-spacing:1px;white-space:nowrap}
.hero .btn{left:113px;top:430px;width:167px;height:43px;border:2px solid var(--white);color:var(--white)}

/* story */
.story-ghost{left:600px;top:790px;font-size:46px;font-weight:800;color:var(--ghost);white-space:nowrap}
.story-title{left:605px;top:812px;font-size:42px;font-weight:800;color:var(--ink);white-space:nowrap}
.story-copy{left:613px;top:890px;width:485px;font-size:13px;line-height:25px}
.story-copy p{margin-bottom:14px}

/* approach */
.approach{position:absolute;left:0;top:1300px;width:1200px;height:635px;background:radial-gradient(ellipse at 50% 40%,#1a8fd8 0%,#0a5fb8 45%,#07307a 100%)}
.approach .section-title{top:72px;color:var(--white)}
.approach .ghost{top:52px;color:rgba(255,255,255,.18)}
.diamond-text{position:absolute;text-align:center;color:var(--white)}
.diamond-text h3{font-size:17px;font-weight:700;letter-spacing:.5px;margin-bottom:8px}
.diamond-text p{font-size:12px;line-height:18px}

/* expertise */
.exp-head{font-size:28px;font-weight:700;color:var(--ink);white-space:nowrap}
.exp-copy{font-size:14px;line-height:25px;width:430px}
.exp-copy p{margin-bottom:16px}
.photo-frame{position:absolute;border-top:6px solid var(--ink);border-left:6px solid var(--ink)}
.photo{position:absolute}

/* stats */
.stats{position:absolute;left:0;top:3473px;width:1200px;height:500px;background:linear-gradient(110deg,#0fa6c0 0%,#1187c4 40%,#1d5cbc 75%,#2048a8 100%)}
.stats h2{position:absolute;left:0;width:1200px;top:100px;text-align:center;font-size:29px;line-height:40px;font-weight:700;color:var(--white)}
.stats .lead{position:absolute;left:0;width:1200px;top:200px;text-align:center;font-size:15px;line-height:26px;color:rgba(255,255,255,.9)}
.stat{position:absolute;top:292px;width:300px;text-align:center;color:var(--white)}
.stat b{display:block;font-size:42px;font-weight:800}
.stat span{display:block;font-size:14px;font-weight:600;margin-top:4px}

/* blog */
.card{position:absolute;top:4120px;width:296px;height:336px;background:var(--white);box-shadow:0 3px 10px rgba(16,40,76,.15)}
.card .thumb{height:200px}
.card h4{margin:20px 22px 0;font-size:12px;line-height:15px;font-weight:700;color:var(--navy)}
.card p{margin:14px 22px 0;font-size:8px;line-height:11px;color:#8a96a8}
.card .more{margin:12px 22px 0;border-left:2px solid var(--teal);padding-left:6px;font-size:8px;font-weight:700;letter-spacing:1px;color:var(--teal)}

/* footer */
.footer{position:absolute;left:0;top:4555px;width:1200px;height:315px;background:var(--navy)}
.footer .rule{position:absolute;top:0;width:1px;height:315px;background:rgba(255,255,255,.3)}
.footer .tag{position:absolute;font-size:10px;font-weight:700;color:var(--white);letter-spacing:1px;writing-mode:vertical-rl}
.footer .links a{position:absolute;left:590px;font-size:12px;color:var(--white);text-decoration:none}
.footer small{position:absolute;font-size:10px;color:var(--white);white-space:nowrap}
</style>
</head>
<body>

<header class="hero" role="img" aria-label="Hand touching a glowing private equity trading screen">
  <svg class="abs" style="left:0;top:0" width="1200" height="740" viewBox="0 0 1200 740">
    <path d="M0 740 L0 725 Q600 610 1200 735 L1200 740 Z" fill="#ffffff"/>
    <path d="M0 728 Q600 604 1200 722" fill="none" stroke="#6a9cc9" stroke-width="4"/>
    <line x1="604" y1="668" x2="604" y2="712" stroke="#6a9cc9" stroke-width="1"/>
  </svg>
  <div class="logo" style="left:110px;top:34px">TORVELLA CAPITAL</div>
  <nav class="nav">
    <a class="active" style="left:646px">EXPERTISE</a>
    <a style="left:803px">STORY</a>
    <a class="contact">CONTACT US</a>
  </nav>
  <div class="abs hero-kicker">TORVELLA CAPITAL</div>
  <h1 class="abs hero-title">BUILT BY FOUNDERS<br>FOR FOUNDERS</h1>
  <div class="btn">Find out more</div>
</header>

<section class="story">
  <svg class="abs" style="left:100px;top:797px" width="468" height="405" viewBox="0 0 468 405" role="img" aria-label="Businessman holding a tablet with financial charts">
    <defs><linearGradient id="hexFill" x1="0" y1="0" x2="1" y2="1"><stop offset="0" stop-color="#cfe0ee"/><stop offset=".5" stop-color="#2a5c9a"/><stop offset="1" stop-color="#0e2444"/></linearGradient></defs>
    <polygon points="117,2 351,2 466,202 351,403 117,403 2,202" fill="#ffffff" stroke="#10284c" stroke-width="2"/>
    <polygon points="127,14 341,14 452,202 341,391 127,391 16,202" fill="url(#hexFill)"/>
  </svg>
  <div class="abs story-ghost">WHO WE ARE</div>
  <h2 class="abs story-title">OUR STORY</h2>
  <div class="abs story-copy">
    <p>Torvella Capital is a venture capital studio firm based in Austin TX with a laser focus on raising solid capital for startups and helping businesses jumpstart their revenue.</p>
    <p>Founded in 2020 by investment expert Marcus Ellery, Torvella Capital combines proven experience in the venture capital field with a data-driven business analysis strategy to secure capital and reinforce revenue streams for startups and established businesses. Born from the idea that the best way to help founders thrive</p>
  </div>
  <div class="btn btn-outline" style="left:617px;top:1133px;width:178px;height:46px;border-color:var(--frame);box-shadow:inset 0 0 0 2px #fff,inset 0 0 0 3px var(--frame)">Learn more</div>
</section>

<section class="approach" role="img" aria-label="Blue network of connected points">
  <div class="ghost">WHO WE ARE</div>
  <h2 class="section-title">OUR APPROACH</h2>
  <svg class="abs" style="left:0;top:0" width="1200" height="635" viewBox="0 0 1200 635">
    <polygon points="300,160 495,355 300,550 105,355" fill="#081a3a" stroke="#0c2e66" stroke-width="4"/>
    <polygon points="915,160 1110,355 915,550 720,355" fill="#0a1d3e" stroke="#0c2e66" stroke-width="4"/>
    <polygon points="608,150 808,350 608,550 408,350" fill="#152840" stroke="#ffffff" stroke-width="8"/>
    <g fill="none" stroke="#ffffff" stroke-width="2">
      <circle cx="300" cy="292" r="16"/><circle cx="300" cy="292" r="6"/>
      <rect x="594" y="272" width="28" height="22" rx="4"/><path d="M600 272 v-6 h16 v6"/>
      <path d="M898 278 h34 l-8 10 h-18 z"/><line x1="915" y1="288" x2="915" y2="300"/>
    </g>
  </svg>
  <div class="diamond-text" style="left:195px;top:320px;width:210px"><h3>EXPERTISE</h3><p>We've built our firm on a bank of insights, knowledge and proficiencies honed over years of working</p></div>
  <div class="diamond-text" style="left:503px;top:335px;width:210px"><h3>COLLABORATION</h3><p>We believe that the best partnerships start with a combined and cooperative approach</p></div>
  <div class="diamond-text" style="left:810px;top:335px;width:210px"><h3>TRUST</h3><p>We know that our clients and our partners know their industry better than we do</p></div>
</section>

<section class="expertise">
  <div class="ghost" style="top:1975px">WHAT WE DO</div>
  <h2 class="section-title" style="top:1996px">AREAS OF EXPERTISE</h2>

  <h3 class="abs exp-head" style="left:138px;top:2145px">NETWORK SUPPORT</h3>
  <div class="abs exp-copy" style="left:142px;top:2195px">
    <p>Lorem ipsum dolor sit amet, consectetur adipiscing elit, sed do eiusmod tempor incididunt ut</p>
    <p>Aagna aliqua Ut enim ad minim veniam, quis nostrud exercitation ullamco laboris nisi ut aliquip ex ea commodo consequat. Duis aute irure dolor</p>
  </div>
  <div class="btn btn-outline" style="left:145px;top:2360px;width:160px;height:41px">Learn more</div>
  <div class="photo-frame" style="left:605px;top:2108px;width:440px;height:320px"></div>
  <div class="photo" style="left:616px;top:2120px;width:425px;height:297px;background:linear-gradient(135deg,#6c7a6a,#c9a88c 55%,#3a4f5c)" role="img" aria-label="Team stacking hands together"></div>

  <svg class="abs" style="left:400px;top:2425px" width="320" height="520" viewBox="0 0 320 520">
    <path d="M15 5 V45 Q15 72 45 72 H255 Q290 72 290 100 V110" fill="none" stroke="#9cc9de" stroke-width="2"/>
    <path d="M297 425 V455 Q297 480 270 480 H52 Q24 480 24 505" fill="none" stroke="#9cc9de" stroke-width="2"/>
  </svg>

  <div class="photo-frame" style="left:120px;top:2538px;width:440px;height:315px"></div>
  <div class="photo" style="left:131px;top:2550px;width:425px;height:296px;background:linear-gradient(135deg,#5d6770,#aab3bb 50%,#3f4852)" role="img" aria-label="Laptop on a desk with marketing strategy keywords"></div>
  <h3 class="abs exp-head" style="left:653px;top:2570px">MARKETING</h3>
  <div class="abs exp-copy" style="left:655px;top:2620px">
    <p>Lorem ipsum dolor sit amet, consectetur adipiscing elit, sed do eiusmod tempor incididunt ut</p>
    <p>Aagna aliqua Ut enim ad minim veniam, quis nostrud exercitation ullamco laboris nisi ut aliquip ex ea commodo consequat. Duis aute irure dolor</p>
  </div>
  <div class="btn btn-outline" style="left:652px;top:2786px;width:160px;height:41px">Learn more</div>

  <h3 class="abs exp-head" style="left:132px;top:3020px">RASING CAPITAL</h3>
  <div class="abs exp-copy" style="left:137px;top:3070px">
    <p>Lorem ipsum dolor sit amet, consectetur adipiscing elit, sed do eiusmod tempor incididunt ut</p>
    <p>Aagna aliqua Ut enim ad minim veniam, quis nostrud exercitation ullamco laboris nisi ut aliquip ex ea commodo consequat. Duis aute irure dolor</p>
  </div>
  <div class="btn btn-outline" style="left:140px;top:3238px;width:160px;height:41px">Learn more</div>
  <div class="photo-frame" style="left:630px;top:2970px;width:440px;height:315px"></div>
  <div class="photo" style="left:642px;top:2983px;width:425px;height:297px;background:linear-gradient(135deg,#1f4f86,#4aa2e0 50%,#0f3a6e)" role="img" aria-label="Hand with glowing rising bar chart"></div>

  <div class="btn" style="left:495px;top:3362px;width:223px;height:53px;background:linear-gradient(90deg,#0b2a5a,#0e8fbf);color:#fff">View more services</div>
</section>

<section class="stats" role="img" aria-label="Tinted city skyscrapers">
  <h2>SED UT PERSPICIATIS UNDE OMNIS ISTE<br>NATUS ERROR SIT</h2>
  <p class="lead">At dolore magna aliqua. Ut enim ad minim veniam, quis nostrud exercitation<br>ullamco laboris nisi ut aliquip a commodo consequat.</p>
  <div class="stat" style="left:162px"><b>$85M</b><span>LOREM IPSUM DOLOR SIT</span></div>
  <div class="stat" style="left:468px"><b>$100M</b><span>LOREM IPSUM DOLOR SIT</span></div>
  <div class="stat" style="left:792px"><b>$205M</b><span>LOREM IPSUM DOLOR SIT</span></div>
</section>

<section class="blog">
  <div class="ghost" style="top:4035px">NEWS &amp; BLOGS</div>
  <h2 class="section-title" style="top:4055px">LATEST BLOGS</h2>
  <article class="card" style="left:150px">
    <div class="thumb" role="img" aria-label="Classroom of students listening to a speaker" style="background:linear-gradient(135deg,#8a6f58,#d8cbb8 60%,#5d4a3c)"></div>
    <h4>Vivamus porttitor neque at volutpat rutrum puruss porttitor neque</h4>
    <p>Lorem ipsum dolor sit amet consectetuer adipiscing elit Nam cursus Morbi ut mi Nullam enim leo</p>
    <div class="more">LEARN MORE</div>
  </article>
  <article class="card" style="left:463px">
    <div class="thumb" role="img" aria-label="Two students studying with a laptop" style="background:linear-gradient(135deg,#cfd6dc,#f0ece6 50%,#6d5446)"></div>
    <h4>Vivamus porttitor neque at volutpat rutrum puruss porttitor neque</h4>
    <p>Lorem ipsum dolor sit amet consectetuer adipiscing elit Nam cursus Morbi ut mi Nullam enim leo</p>
    <div class="more">LEARN MORE</div>
  </article>
  <article class="card" style="left:773px">
    <div class="thumb" role="img" aria-label="Student holding books on a campus lawn" style="background:linear-gradient(135deg,#7a9a5a,#b6c88e 45%,#7a2a2a)"></div>
    <h4>Vivamus porttitor neque at volutpat rutrum puruss porttitor neque</h4>
    <p>Lorem ipsum dolor sit amet consectetuer adipiscing elit Nam cursus Morbi ut mi Nullam enim leo</p>
    <div class="more">LEARN MORE</div>
  </article>
</section>

<footer class="footer">
  <div class="logo" style="left:140px;top:80px">TORVELLA CAPITAL</div>
  <svg class="abs" style="left:140px;top:122px" width="135" height="30" viewBox="0 0 135 30" aria-label="Social links">
    <circle cx="13" cy="15" r="12" fill="#fff"/><circle cx="47" cy="15" r="12" fill="#fff"/><circle cx="81" cy="15" r="12" fill="#fff"/><circle cx="115" cy="15" r="12" fill="#fff"/>
  </svg>
  <small style="left:140px;top:185px">Copyright © 2022 Torvella Capital</small>
  <small style="left:140px;top:213px">Privacy Policy &nbsp;|&nbsp; Terms of Use</small>
  <div class="rule" style="left:562px"></div>
  <div class="tag" style="left:538px;top:60px">COMPANY</div>
  <nav class="links">
    <a style="top:80px">Home</a><a style="top:106px">Expertise</a><a style="top:132px">Story</a><a style="top:158px">Approach</a><a style="top:184px">Contact</a>
  </nav>
  <div class="rule" style="left:833px"></div>
  <div class="tag" style="left:808px;top:60px">CONTACT</div>
  <svg class="abs" style="left:858px;top:66px" width="24" height="92" viewBox="0 0 24 92" fill="none" stroke="#fff" stroke-width="1.6" stroke-linejoin="round">
    <path d="M5 3 l4 -1 3 5 -2.5 2.5 q2 5 7 7.5 l2.5 -2.5 5 3 -1 4 q-13 1 -18 -18.5z"/>
    <rect x="2" y="74" width="19" height="13"/><path d="M2 74 l9.5 7 9.5 -7"/>
  </svg>
  <small style="left:897px;top:68px;font-weight:700;font-size:11px">Phone</small>
  <small style="left:897px;top:86px;font-size:11px">555-014-2200</small>
  <small style="left:897px;top:128px;font-weight:700;font-size:11px">Email</small>
  <small style="left:897px;top:146px;font-size:11px;text-decoration:underline">info@torvellacapital.com</small>
</footer>

</body>
</html>
```